Indy Film Production Company/Studio

We need a business card designed from an existing logo. We are a digital studio/production company that caters to creating genre entertainment, like Action, Horror, and martial arts. The card along with the logo will be used to Brand the company from letter heads to banners. The design will also be used for postcards and Brochures. It should be professional and masculine.
Updates

Thank you to all the designers who have participated. I'm narrowing down who it will be. Thank you again.

Target Market(s)

Investors, Networks, Producers, and actors

Industry/Entity Type

Film Production

Contact Information for Business Card

Benedict Harlowe
Producer/Writer/Director
www.pelvarmotionworks.com

Requirements
Must have
• Website address, Facebook icon and Twitter icon possibly in the back of the card.
Nice to have
• Logline of Company: Follow The Action.

```html
<!DOCTYPE html>
<html lang="en">
<head>
<meta charset="utf-8">
<title>Pelvar Motion Works — Business Card</title>
<link rel="stylesheet" href="https://fonts.googleapis.com/css2?family=Questrial&display=swap">
<style>
  :root {
    --stage: #2b2a29;
    --card: #141414;
    --card-edge: #0c0c0c;
    --ink: #e6e6e6;
    --ink-soft: #b9b9b9;
    --glow-hot: #f4c58a;
    --glow-mid: #8a4c1e;
    --glow-dark: #2a1709;
    --photo-light: #4a4a4a;
    --photo-dark: #101010;
  }
  * { box-sizing: border-box; margin: 0; padding: 0; }
  html, body {
    width: 1200px; height: 727px; overflow: hidden;
    background: var(--stage);
    font-family: "Questrial", "Century Gothic", sans-serif;
    color: var(--ink);
  }
  .stage {
    position: relative; width: 1200px; height: 727px;
    display: flex; align-items: center; justify-content: center; gap: 40px;
  }
  .card {
    position: relative; width: 540px; height: 310px;
    background: var(--card); border: 1px solid var(--card-edge);
    overflow: hidden;
    box-shadow: 0 12px 30px rgba(0,0,0,.45);
  }

  /* Front */
  .front__artwork {
    position: absolute; left: 40px; top: 20px; width: 460px; height: 230px;
    background: radial-gradient(ellipse at 50% 45%, var(--glow-hot) 0%, var(--glow-mid) 30%, var(--glow-dark) 62%, transparent 78%);
    opacity: .9;
  }
  .front__name {
    position: absolute; left: 0; right: 0; top: 180px;
    text-align: center; font-size: 24px; letter-spacing: 3px;
    text-transform: uppercase; color: var(--ink);
  }
  .front__web {
    position: absolute; left: 40px; bottom: 34px;
    font-size: 15px; color: var(--ink-soft); letter-spacing: .5px;
  }
  .front__social {
    position: absolute; right: 34px; bottom: 32px; display: flex; gap: 6px;
  }
  .front__social span {
    width: 20px; height: 20px; border-radius: 3px; background: var(--ink-soft);
  }

  /* Back */
  .back__photo {
    position: absolute; right: 0; top: 0; width: 230px; height: 100%;
    background: radial-gradient(ellipse at 60% 65%, var(--photo-light) 0%, #262626 35%, var(--photo-dark) 75%);
  }
  .back__logo {
    position: absolute; left: 30px; top: 28px;
    font-size: 26px; letter-spacing: 2px; text-transform: uppercase; color: var(--ink);
    line-height: 1.1;
  }
  .back__logo small { display: block; font-size: 12px; letter-spacing: 2px; }
  .back__person { position: absolute; left: 30px; top: 120px; }
  .back__name { font-size: 24px; color: var(--ink); }
  .back__role { font-size: 15px; color: var(--ink-soft); margin-top: 2px; }
  .back__contacts {
    position: absolute; left: 30px; top: 190px;
    list-style: none; font-size: 13.5px; color: var(--ink-soft); line-height: 1.75;
  }
  .back__contacts li { display: flex; align-items: center; gap: 7px; }
  .back__contacts .row { gap: 22px; }
  .back__contacts svg { width: 13px; height: 13px; fill: var(--ink-soft); }
</style>
</head>
<body>
<main class="stage">

  <section class="card front" aria-label="Card front">
    <div class="front__artwork" role="img" aria-label="Glowing cinematic company logo artwork with warm sparks"></div>
    <h1 class="front__name">Pelvar Motion Works</h1>
    <p class="front__web">www.pelvarmotionworks.com</p>
    <div class="front__social" aria-label="Social links"><span></span><span></span><span></span></div>
  </section>

  <section class="card back" aria-label="Card back">
    <div class="back__photo" role="img" aria-label="Close-up photograph of a professional video camera lens"></div>
    <div class="back__logo">PMW<small>Pelvar Motion Works</small></div>
    <div class="back__person">
      <h2 class="back__name">Benedict Harlowe</h2>
      <p class="back__role">Producer/Writer/Director</p>
    </div>
    <ul class="back__contacts">
      <li class="row">
        <span style="display:flex;align-items:center;gap:7px">
          <svg viewBox="0 0 16 16"><path d="M3 1h3l1.5 4-2 1.2a9 9 0 0 0 4.3 4.3L11 8.5l4 1.5v3a2 2 0 0 1-2 2A12 12 0 0 1 1 3a2 2 0 0 1 2-2z"/></svg>000 000 0000
        </span>
        <span style="display:flex;align-items:center;gap:7px">
          <svg viewBox="0 0 16 16"><path d="M1 3h14v10H1z M1 3l7 6 7-6" fill="none" stroke="#b9b9b9" stroke-width="1.5"/></svg>hello@pelvarmotionworks.com
        </span>
      </li>
      <li>https://social.pelvarmotionworks.com/news</li>
      <li>www.pelvarmotionworks.com/community</li>
    </ul>
  </section>

</main>
</body>
</html>
```